Japanese Rice Food Package Label

- We are launching Japanese food products to the outdoor community.
- Made in Japan
- We will have multiple flavors of rice but want to keep the package label almost the same and only replace the flavor text (e.g., Mixed Rice, Curry Rice, etc)
- We like simple designs inspired by Japan.
- Label size: 105 mm x148 mm
- Our brand: YOBEN https://yoben.co/
- Video message: https://www.vidqo.com/share/3f51b07a9e2c4d6891a0c7e5b2d94f18

```html
<!DOCTYPE html>
<html lang="en">
<head>
<meta charset="utf-8">
<title>YOBEN Rice Pouch Labels</title>
<link href="https://fonts.googleapis.com/css2?family=Roboto:wght@300;400;500&display=swap" rel="stylesheet">
<style>
  :root {
    --teal: #0ba896;
    --mint: #a9e7e0;
    --mint-soft: #dcf6f3;
    --outline: #b4efe8;
    --paper: #ffffff;
  }
  * { margin: 0; padding: 0; box-sizing: border-box; }
  html, body { width: 1200px; height: 1200px; overflow: hidden; background: var(--paper); }
  body { position: relative; font-family: "Roboto", Arial, sans-serif; }

  .pouch { position: absolute; left: 366px; width: 482px; height: 448px; }
  .pouch--mixed { top: 89px; }
  .pouch--curry { top: 671px; }

  .pouch__outline { position: absolute; inset: 0; width: 482px; height: 448px; }

  .pouch__url {
    position: absolute; left: 358px; top: 17px; width: 108px; height: 29px;
    background: var(--teal); color: var(--paper);
    font-size: 21px; font-weight: 400; line-height: 29px; text-align: center;
    letter-spacing: 0.3px;
  }

  .label {
    position: absolute; left: 19px; top: 105px; width: 444px; height: 314px;
    border: 3px solid var(--teal); overflow: hidden; background: var(--paper);
  }

  .label__petals-right {
    position: absolute; left: 296px; top: 8px; width: 136px; height: 196px;
    background: var(--mint-soft); border-radius: 40% 0 0 60%;
  }
  .label__petals-left {
    position: absolute; left: 10px; top: 190px; width: 96px; height: 116px;
    background: var(--mint-soft); border-radius: 60% 40% 0 0;
  }

  .label__flower {
    position: absolute; left: 154px; top: 16px; width: 136px; height: 130px;
    background: var(--mint-soft); border: 2px solid var(--teal); border-radius: 50%;
  }

  .label__tagline {
    position: absolute; right: 17px; top: 10px;
    color: var(--teal); font-size: 14px; font-weight: 400;
    letter-spacing: 1.2px; line-height: 17px; text-align: right;
  }

  .label__side-note {
    position: absolute; left: 10px; top: 14px; height: 124px;
    writing-mode: vertical-rl; transform: rotate(180deg);
    color: var(--teal); font-size: 12.5px; letter-spacing: 0.8px; text-align: right;
  }

  .label__flavor {
    position: absolute; left: 122px; top: 162px; width: 200px; height: 40px;
    background: var(--mint); color: var(--paper);
    font-size: 29px; font-weight: 400; letter-spacing: 1.5px;
    line-height: 40px; text-align: center;
  }

  .label__origin {
    position: absolute; left: 0; right: 0; top: 207px;
    color: var(--mint); font-size: 14px; font-weight: 300;
    letter-spacing: 1px; text-align: center;
  }

  .label__brand {
    position: absolute; left: 0; right: 0; top: 224px;
    color: var(--teal); font-size: 74px; font-weight: 500;
    letter-spacing: 3px; text-align: center; line-height: 86px;
  }
</style>
</head>
<body>

<section class="pouch pouch--mixed">
  <svg class="pouch__outline" viewBox="0 0 482 448" aria-hidden="true">
    <path d="M22 2 H460 Q480 2 480 22 V56 L472 64 L480 72 V300 L478 304 V405 Q478 430 450 438 L390 446 H92 L32 438 Q4 430 4 405 V304 L2 300 V72 L10 64 L2 56 V22 Q2 2 22 2 Z"
          fill="none" stroke="var(--outline)" stroke-width="3"/>
    <rect x="228" y="8" width="26" height="19" rx="8" fill="none" stroke="var(--outline)" stroke-width="3"/>
  </svg>
  <div class="pouch__url">yoben.co</div>
  <div class="label">
    <div class="label__petals-right" role="img" aria-label="Faint blossom petal decoration"></div>
    <div class="label__petals-left" role="img" aria-label="Faint blossom petal decoration"></div>
    <div class="label__flower" role="img" aria-label="Blossom illustration"></div>
    <p class="label__tagline">READY TO EAT<br>IN 10 MINUTES</p>
    <p class="label__side-note">JUST ADD WATER</p>
    <p class="label__flavor">MIXED RICE</p>
    <p class="label__origin">MADE IN JAPAN</p>
    <p class="label__brand">YOBEN</p>
  </div>
</section>

<section class="pouch pouch--curry">
  <svg class="pouch__outline" viewBox="0 0 482 448" aria-hidden="true">
    <path d="M22 2 H460 Q480 2 480 22 V56 L472 64 L480 72 V300 L478 304 V405 Q478 430 450 438 L390 446 H92 L32 438 Q4 430 4 405 V304 L2 300 V72 L10 64 L2 56 V22 Q2 2 22 2 Z"
          fill="none" stroke="var(--outline)" stroke-width="3"/>
    <rect x="228" y="8" width="26" height="19" rx="8" fill="none" stroke="var(--outline)" stroke-width="3"/>
  </svg>
  <div class="pouch__url">yoben.co</div>
  <div class="label">
    <div class="label__petals-right" role="img" aria-label="Faint blossom petal decoration"></div>
    <div class="label__petals-left" role="img" aria-label="Faint blossom petal decoration"></div>
    <div class="label__flower" role="img" aria-label="Blossom illustration"></div>
    <p class="label__tagline">READY TO EAT<br>IN 10 MINUTES</p>
    <p class="label__side-note">JUST ADD WATER</p>
    <p class="label__flavor">CURRY RICE</p>
    <p class="label__origin">MADE IN JAPAN</p>
    <p class="label__brand">YOBEN</p>
  </div>
</section>

</body>
</html>
```